Nonna's Vellato

I am looking to design a label to be used on a glass jar for packaging a very special spice that has been used in our family for generations. The spice is excellent on meats, burgers, poultry, fish, and more.

The name of the spice is "Nonna's Famous Vellato"

Design should be traditional, with an Italian feel.

Total circumference of the jar is 10"
Height of jar is 4"

Some of the glass should not be covered to reveal color of spice inside.

Target Market(s)

Female 25-75

```html
<!DOCTYPE html>
<html lang="en">
<head>
<meta charset="utf-8">
<title>Nonna's Famous Vellato – Jar Label</title>
<link rel="stylesheet" href="https://fonts.googleapis.com/css2?family=Arimo&family=Lobster&family=Tinos:wght@400;700&display=swap">
<style>
  :root {
    --label-red: #d22a12;
    --band-green: #009041;
    --ink: #000000;
    --paper: #ffffff;
    --ribbon-red: #e8193f;
    --ribbon-shade: #a80f2b;
    --sage-dark: #5f7a60;
    --sage-light: #c3d3bf;
  }
  html, body {
    margin: 0;
    padding: 0;
    width: 1200px;
    height: 860px;
    overflow: hidden;
    background: var(--paper);
  }
  .label {
    display: block;
    width: 1200px;
    height: 860px;
  }
  .brand-name {
    font-family: "Tinos", "Times New Roman", serif;
    font-weight: 700;
    font-size: 112px;
    fill: var(--paper);
    stroke: var(--ink);
    stroke-width: 3px;
    paint-order: stroke;
  }
  .famous-word {
    font-family: "Lobster", cursive;
    font-size: 100px;
    fill: var(--paper);
  }
  .seasoning-title {
    font-family: "Tinos", "Times New Roman", serif;
    font-size: 72px;
    font-variant: small-caps;
    fill: var(--paper);
    stroke: var(--ink);
    stroke-width: 4px;
    paint-order: stroke;
    letter-spacing: 1px;
  }
  .usage-line {
    font-family: "Arimo", Arial, sans-serif;
    font-size: 40px;
    fill: var(--paper);
  }
  .net-weight {
    font-family: "Arimo", Arial, sans-serif;
    font-size: 34px;
    fill: var(--paper);
  }
</style>
</head>
<body>
<svg class="label" viewBox="0 0 1476 1058" preserveAspectRatio="none" xmlns="http://www.w3.org/2000/svg">
  <defs>
    <linearGradient id="oval-fade" x1="0" y1="0" x2="0" y2="1">
      <stop offset="0.55" stop-color="#ffffff"/>
      <stop offset="0.8" stop-color="#b9dfb9"/>
      <stop offset="1" stop-color="#2f9a3c"/>
    </linearGradient>
    <radialGradient id="window-sage" cx="0.5" cy="0.55" r="0.6">
      <stop offset="0" stop-color="var(--sage-light)"/>
      <stop offset="1" stop-color="var(--sage-dark)"/>
    </radialGradient>
    <radialGradient id="herb-tone" cx="0.5" cy="0.45" r="0.55">
      <stop offset="0" stop-color="#4f7a3c"/>
      <stop offset="1" stop-color="#8fae86" stop-opacity="0"/>
    </radialGradient>
    <linearGradient id="ribbon-sheen" x1="0" y1="0" x2="1" y2="0">
      <stop offset="0" stop-color="#c4102f"/>
      <stop offset="0.3" stop-color="var(--ribbon-red)"/>
      <stop offset="0.6" stop-color="#f0557a"/>
      <stop offset="1" stop-color="#d3133a"/>
    </linearGradient>
    <path id="usage-arc" d="M 384,530 A 355 470 0 0 0 1094,530"/>
    <path id="seasoning-arc" d="M 460,560 A 285 345 0 0 0 1030,560"/>
  </defs>

  <!-- horizontal bands -->
  <g class="bands">
    <rect class="band-red" x="0" y="137" width="1476" height="748" fill="var(--label-red)"/>
    <rect class="band-rule" x="0" y="165" width="1476" height="690" fill="var(--ink)"/>
    <rect class="band-green" x="0" y="180" width="1476" height="660" fill="var(--band-green)"/>
  </g>

  <!-- central oval badge -->
  <g class="badge">
    <ellipse cx="739" cy="530" rx="382" ry="510" fill="var(--label-red)"/>
    <ellipse cx="739" cy="530" rx="370" ry="498" fill="var(--ink)"/>
    <ellipse cx="739" cy="500" rx="330" ry="455" fill="url(#oval-fade)"/>
    <ellipse cx="745" cy="480" rx="230" ry="300" fill="#4a5a4a"/>
    <ellipse cx="745" cy="482" rx="222" ry="292" fill="url(#window-sage)"/>
  </g>

  <!-- herb sprig area -->
  <ellipse class="herb-photo" role="img" aria-label="Photo of a fresh herb sprig with green leaves"
           cx="760" cy="550" rx="150" ry="190" fill="url(#herb-tone)"/>

  <!-- curved usage line -->
  <text class="usage-line"><textPath href="#usage-arc" startOffset="50%" text-anchor="middle">Excellent on meats, burgers, poultry, fish, and more</textPath></text>

  <!-- curved seasoning title -->
  <text class="seasoning-title"><textPath href="#seasoning-arc" startOffset="50%" text-anchor="middle">Special Seasoning</textPath></text>

  <!-- net weight pill -->
  <g class="net-weight-tag">
    <rect x="610" y="745" width="270" height="54" rx="27" fill="var(--ink)"/>
    <text class="net-weight" x="745" y="784" text-anchor="middle">Net Wt. 1.75 oz</text>
  </g>

  <!-- ribbon banner -->
  <g class="ribbon">
    <path d="M 362,200 L 410,196 L 400,250 Z" fill="var(--ribbon-shade)"/>
    <path d="M 362,200 Q 720,250 1092,135 L 1098,320 Q 720,300 348,492 Q 368,350 362,200 Z" fill="url(#ribbon-sheen)"/>
    <text class="brand-name" x="0" y="0" text-anchor="middle" textLength="700" lengthAdjust="spacingAndGlyphs" transform="translate(735 400) rotate(-10)">Nonna's Vellato</text>
  </g>

  <!-- famous tab -->
  <g class="famous-tab">
    <path d="M 660,60 L 985,46 Q 1006,40 1004,60 L 990,200 Q 985,213 968,212 L 672,212 Z" fill="var(--ink)"/>
    <text class="famous-word" x="0" y="0" text-anchor="middle" transform="translate(828 172) rotate(-4)">Famous</text>
  </g>
</svg>
</body>
</html>
```